label design for cannabis

label template 4"x5.5" for a Massachusetts cannabis beverage product. labels will be transparent and placed on a blue (pantone 306C) bag.
https://www.fravostones.com/

Target Market(s)

cannabis customers in MA, 21+

Industry/Entity Type

cannabis consumer product

Font styles to use
Other font styles liked:
• DIN

Colors
0094D4
00A9DD
6FCCEA
C7EBF8
E9F6FB

Requirements
Must have
• label design with fravo logo, flavor (lemon, lime, plain, and coffee). 306C pantone for background and 11-0601 TCX for text. font=DINackground.
Nice to have
• tray icon, illustrated ice cubes in white (clear), yellow (lemon), green (lime) and brown (coffee)
Should not have
• no cartoonish characters

```html
<!DOCTYPE html>
<html lang="en">
<head>
<meta charset="utf-8">
<title>fravo infused ice cubes – label set</title>
<link rel="stylesheet" href="https://fonts.googleapis.com/css2?family=Barlow+Condensed:wght@500;600&family=Barlow+Semi+Condensed:wght@700;800&display=swap">
<style>
  :root {
    --page-bg: #ebebeb;
    --ink-dark: #1a1a1a;
    --bag-blue: #00b3e0;
    --label-white: #ffffff;
    --flavor-classic: #ffffff;
    --flavor-coffee: #7a3a14;
    --flavor-lime: #c2f400;
    --flavor-lemon: #f0f000;
  }
  * { box-sizing: border-box; margin: 0; padding: 0; }
  html, body { width: 1200px; height: 1035px; overflow: hidden; }
  body { background: var(--page-bg); position: relative; font-family: "Barlow Condensed", "Arial Narrow", sans-serif; }

  .row-heading {
    position: absolute; left: 0; width: 1200px; text-align: center;
    font-family: "Barlow Semi Condensed", "Arial Narrow", sans-serif; font-weight: 800;
    font-size: 32px; color: var(--ink-dark); line-height: 1;
  }
  .row-heading--plain { top: 67px; }
  .row-heading--marked { top: 556px; }

  .label {
    position: absolute; width: 268px; height: 369px;
    background: var(--bag-blue); color: var(--label-white);
    box-shadow: 4px 6px 10px rgba(0,0,0,.22);
  }
  .label--classic { --flavor: var(--flavor-classic); }
  .label--coffee  { --flavor: var(--flavor-coffee); }
  .label--lime    { --flavor: var(--flavor-lime); }
  .label--lemon   { --flavor: var(--flavor-lemon); }

  .label__brand {
    position: absolute; top: 18px; left: 0; width: 100%; text-align: center;
    font-weight: 600; font-size: 100px; line-height: 1; letter-spacing: -1px;
  }
  .label__tagline {
    position: absolute; top: 111px; left: 0; width: 100%; text-align: center;
    font-weight: 500; font-size: 29px; line-height: 1;
  }
  .label__cubes {
    position: absolute; top: 171px; left: 90px; width: 88px; height: 55px;
    border-radius: 45%;
    background: radial-gradient(ellipse at center, var(--flavor) 0%, transparent 72%);
    opacity: .55;
  }
  .label__flavor {
    position: absolute; top: 232px; left: 0; width: 100%; text-align: center;
    font-family: "Barlow Semi Condensed", "Arial Narrow", sans-serif; font-weight: 800;
    font-size: 37px; line-height: 1; color: var(--flavor);
  }
  .label__rule {
    position: absolute; top: 269px; left: 74px; width: 120px; height: 2px;
    background: var(--label-white);
  }
  .label__dose {
    position: absolute; top: 273px; left: 0; width: 100%; text-align: center;
    font-family: "Barlow Semi Condensed", "Arial Narrow", sans-serif; font-weight: 700;
    font-size: 11px; line-height: 14px; color: var(--flavor);
  }
  .label__tray { position: absolute; top: 302px; left: 71px; width: 127px; height: 36px; }
  .label__tray-text {
    position: absolute; top: 302px; left: 71px; width: 127px; height: 16px;
    text-align: center; line-height: 16px;
    font-family: "Barlow Semi Condensed", "Arial Narrow", sans-serif; font-weight: 700; font-size: 11px;
  }
  .label__warning { position: absolute; }
  .label__warning--thc { left: 12px; top: 322px; width: 34px; height: 30px; }
  .label__warning--kids { left: 219px; top: 322px; width: 39px; height: 39px; }
  .label__warning-text {
    position: absolute; color: var(--label-white); text-align: center;
    font-family: "Barlow Condensed", "Arial Narrow", sans-serif; font-weight: 500;
    font-size: 7px; line-height: 8px;
  }
  .label__warning-text--thc { left: 6px; top: 355px; width: 46px; }
  .label__warning-text--kids { left: 219px; top: 332px; width: 39px; }
</style>
</head>
<body>

<h2 class="row-heading row-heading--plain">Without Logo</h2>
<h2 class="row-heading row-heading--marked">With Logo</h2>

<section class="label label--classic" style="left:45px;top:121px">
  <div class="label__brand">fravo</div>
  <div class="label__tagline">infused ice cubes</div>
  <div class="label__cubes" role="img" aria-label="Line illustration of three ice cubes in white"></div>
  <div class="label__flavor">classic</div>
  <div class="label__rule"></div>
  <div class="label__dose">5mg per cube</div>
  <svg class="label__tray" viewBox="0 0 127 36" fill="none" stroke="#fff" stroke-width="2"><rect x="1" y="1" width="125" height="14"/><path d="M5 15 L8 34 H24 L27 15 M29 15 L32 34 H48 L51 15 M53 15 L56 34 H72 L75 15 M77 15 L80 34 H96 L99 15 M101 15 L104 34 H120 L123 15"/></svg>
  <div class="label__tray-text">50mg per tray</div>
</section>

<section class="label label--coffee" style="left:326px;top:121px">
  <div class="label__brand">fravo</div>
  <div class="label__tagline">infused ice cubes</div>
  <div class="label__cubes" role="img" aria-label="Line illustration of three ice cubes in coffee brown"></div>
  <div class="label__flavor">coffee</div>
  <div class="label__rule"></div>
  <div class="label__dose">5mg per cube</div>
  <svg class="label__tray" viewBox="0 0 127 36" fill="none" stroke="#fff" stroke-width="2"><rect x="1" y="1" width="125" height="14"/><path d="M5 15 L8 34 H24 L27 15 M29 15 L32 34 H48 L51 15 M53 15 L56 34 H72 L75 15 M77 15 L80 34 H96 L99 15 M101 15 L104 34 H120 L123 15"/></svg>
  <div class="label__tray-text">50mg per tray</div>
</section>

<section class="label label--lime" style="left:606px;top:121px">
  <div class="label__brand">fravo</div>
  <div class="label__tagline">infused ice cubes</div>
  <div class="label__cubes" role="img" aria-label="Line illustration of three ice cubes in lime green"></div>
  <div class="label__flavor">lime</div>
  <div class="label__rule"></div>
  <div class="label__dose">5mg per cube</div>
  <svg class="label__tray" viewBox="0 0 127 36" fill="none" stroke="#fff" stroke-width="2"><rect x="1" y="1" width="125" height="14"/><path d="M5 15 L8 34 H24 L27 15 M29 15 L32 34 H48 L51 15 M53 15 L56 34 H72 L75 15 M77 15 L80 34 H96 L99 15 M101 15 L104 34 H120 L123 15"/></svg>
  <div class="label__tray-text">50mg per tray</div>
</section>

<section class="label label--lemon" style="left:888px;top:121px">
  <div class="label__brand">fravo</div>
  <div class="label__tagline">infused ice cubes</div>
  <div class="label__cubes" role="img" aria-label="Line illustration of three ice cubes in lemon yellow"></div>
  <div class="label__flavor">lemon</div>
  <div class="label__rule"></div>
  <div class="label__dose">5mg per cube</div>
  <svg class="label__tray" viewBox="0 0 127 36" fill="none" stroke="#fff" stroke-width="2"><rect x="1" y="1" width="125" height="14"/><path d="M5 15 L8 34 H24 L27 15 M29 15 L32 34 H48 L51 15 M53 15 L56 34 H72 L75 15 M77 15 L80 34 H96 L99 15 M101 15 L104 34 H120 L123 15"/></svg>
  <div class="label__tray-text">50mg per tray</div>
</section>

<section class="label label--classic" style="left:45px;top:604px">
  <div class="label__brand">fravo</div>
  <div class="label__tagline">infused ice cubes</div>
  <div class="label__cubes" role="img" aria-label="Line illustration of three ice cubes in white"></div>
  <div class="label__flavor">classic</div>
  <div class="label__rule"></div>
  <div class="label__dose">5mg per cube</div>
  <svg class="label__tray" viewBox="0 0 127 36" fill="none" stroke="#fff" stroke-width="2"><rect x="1" y="1" width="125" height="14"/><path d="M5 15 L8 34 H24 L27 15 M29 15 L32 34 H48 L51 15 M53 15 L56 34 H72 L75 15 M77 15 L80 34 H96 L99 15 M101 15 L104 34 H120 L123 15"/></svg>
  <div class="label__tray-text">50mg per tray</div>
  <svg class="label__warning label__warning--thc" viewBox="0 0 34 30" fill="none" stroke="#fff" stroke-width="2"><path d="M17 2 L32 28 H2 Z"/></svg>
  <div class="label__warning-text label__warning-text--thc">CONTAINS THC</div>
  <svg class="label__warning label__warning--kids" viewBox="0 0 39 39" fill="none" stroke="#fff" stroke-width="2"><path d="M12 1 H27 L38 12 V27 L27 38 H12 L1 27 V12 Z"/></svg>
  <div class="label__warning-text label__warning-text--kids">NOT SAFE<br>FOR KIDS</div>
</section>

<section class="label label--coffee" style="left:326px;top:604px">
  <div class="label__brand">fravo</div>
  <div class="label__tagline">infused ice cubes</div>
  <div class="label__cubes" role="img" aria-label="Line illustration of three ice cubes in coffee brown"></div>
  <div class="label__flavor">coffee</div>
  <div class="label__rule"></div>
  <div class="label__dose">5mg per cube</div>
  <svg class="label__tray" viewBox="0 0 127 36" fill="none" stroke="#fff" stroke-width="2"><rect x="1" y="1" width="125" height="14"/><path d="M5 15 L8 34 H24 L27 15 M29 15 L32 34 H48 L51 15 M53 15 L56 34 H72 L75 15 M77 15 L80 34 H96 L99 15 M101 15 L104 34 H120 L123 15"/></svg>
  <div class="label__tray-text">50mg per tray</div>
  <svg class="label__warning label__warning--thc" viewBox="0 0 34 30" fill="none" stroke="#fff" stroke-width="2"><path d="M17 2 L32 28 H2 Z"/></svg>
  <div class="label__warning-text label__warning-text--thc">CONTAINS THC</div>
  <svg class="label__warning label__warning--kids" viewBox="0 0 39 39" fill="none" stroke="#fff" stroke-width="2"><path d="M12 1 H27 L38 12 V27 L27 38 H12 L1 27 V12 Z"/></svg>
  <div class="label__warning-text label__warning-text--kids">NOT SAFE<br>FOR KIDS</div>
</section>

<section class="label label--lime" style="left:606px;top:604px">
  <div class="label__brand">fravo</div>
  <div class="label__tagline">infused ice cubes</div>
  <div class="label__cubes" role="img" aria-label="Line illustration of three ice cubes in lime green"></div>
  <div class="label__flavor">lime</div>
  <div class="label__rule"></div>
  <div class="label__dose">5mg per cube</div>
  <svg class="label__tray" viewBox="0 0 127 36" fill="none" stroke="#fff" stroke-width="2"><rect x="1" y="1" width="125" height="14"/><path d="M5 15 L8 34 H24 L27 15 M29 15 L32 34 H48 L51 15 M53 15 L56 34 H72 L75 15 M77 15 L80 34 H96 L99 15 M101 15 L104 34 H120 L123 15"/></svg>
  <div class="label__tray-text">50mg per tray</div>
  <svg class="label__warning label__warning--thc" viewBox="0 0 34 30" fill="none" stroke="#fff" stroke-width="2"><path d="M17 2 L32 28 H2 Z"/></svg>
  <div class="label__warning-text label__warning-text--thc">CONTAINS THC</div>
  <svg class="label__warning label__warning--kids" viewBox="0 0 39 39" fill="none" stroke="#fff" stroke-width="2"><path d="M12 1 H27 L38 12 V27 L27 38 H12 L1 27 V12 Z"/></svg>
  <div class="label__warning-text label__warning-text--kids">NOT SAFE<br>FOR KIDS</div>
</section>

<section class="label label--lemon" style="left:888px;top:604px">
  <div class="label__brand">fravo</div>
  <div class="label__tagline">infused ice cubes</div>
  <div class="label__cubes" role="img" aria-label="Line illustration of three ice cubes in lemon yellow"></div>
  <div class="label__flavor">lemon</div>
  <div class="label__rule"></div>
  <div class="label__dose">5mg per cube</div>
  <svg class="label__tray" viewBox="0 0 127 36" fill="none" stroke="#fff" stroke-width="2"><rect x="1" y="1" width="125" height="14"/><path d="M5 15 L8 34 H24 L27 15 M29 15 L32 34 H48 L51 15 M53 15 L56 34 H72 L75 15 M77 15 L80 34 H96 L99 15 M101 15 L104 34 H120 L123 15"/></svg>
  <div class="label__tray-text">50mg per tray</div>
  <svg class="label__warning label__warning--thc" viewBox="0 0 34 30" fill="none" stroke="#fff" stroke-width="2"><path d="M17 2 L32 28 H2 Z"/></svg>
  <div class="label__warning-text label__warning-text--thc">CONTAINS THC</div>
  <svg class="label__warning label__warning--kids" viewBox="0 0 39 39" fill="none" stroke="#fff" stroke-width="2"><path d="M12 1 H27 L38 12 V27 L27 38 H12 L1 27 V12 Z"/></svg>
  <div class="label__warning-text label__warning-text--kids">NOT SAFE<br>FOR KIDS</div>
</section>

</body>
</html>
```